3 Graphics to be used on our Web Site and Blogs

3 Separate graphics to be used in our marketing for our Business Architecture Consulting Organization. The first graphics is used on the web site mock-up and is the guy drawing the model. I have included a file of what the model that is being drawn should contain. I would like that graphic to be polished up and have a female used. The second graphic should bring our tag line to life. The tag line is (People + Process + Technology) * Planning = Success. The third graphic should show an iterative methodology of with 5 separate steps Assessment, Envision, Design, Evaluate, Implement. This graphic should be a circular representation that never ends and continuously improves.

Target Market(s)

Small Business Owners and Mid-Level Managers in large corporations

Industry/Entity Type

Consulting

Requirements
Must have
• Professional look and feel based on the target audience.
Nice to have
• Set of graphics should all go together to help form our brand. I included our logo as another piece of the puzzle. The web site is just a mock-up and it would be nice to see how the graphics could be used in the mock-up.

```html
<!DOCTYPE html>
<html lang="en">
<head>
<meta charset="utf-8">
<title>Methodology Graphics Set</title>
<link rel="stylesheet" href="https://fonts.googleapis.com/css2?family=Arimo:wght@400;700&display=swap">
<style>
  :root {
    --blue-light: #2aa3e6;
    --blue-dark: #0a5ea8;
    --blue-text: #0b67b2;
    --orange-light: #f9a51e;
    --orange-dark: #f15a22;
    --ink: #222222;
    --rule: #555555;
    --grid: #c4c4c4;
    --paper: #ffffff;
  }
  html, body {
    margin: 0;
    padding: 0;
    width: 1200px;
    height: 3859px;
    overflow: hidden;
    background: var(--paper);
  }
  .sheet { display: block; width: 1200px; height: 3859px; }
  .sheet text { font-family: "Arimo", Arial, sans-serif; }
  .caption { font-size: 10px; fill: var(--ink); }
  .rule { stroke: var(--rule); stroke-width: 1; }
  .box-copy { font-size: 14.5px; font-weight: 700; fill: var(--blue-text); }
  .tab-label { font-size: 17px; font-weight: 700; fill: #fff; text-anchor: middle; }
  .bar-label { font-size: 21px; font-weight: 700; fill: #fff; text-anchor: middle; }
  .head-label { font-size: 20px; font-weight: 700; fill: #fff; text-anchor: middle; }
  .pill-copy { font-weight: 700; fill: #fff; }
  .center { text-anchor: middle; }
  .cycle-label { font-size: 25px; font-weight: 700; fill: var(--blue-text); }
  .methodology-label { font-size: 27px; font-weight: 700; fill: var(--blue-dark); text-anchor: middle; }
</style>
</head>
<body>
<svg class="sheet" viewBox="0 0 740 2382" xmlns="http://www.w3.org/2000/svg" xmlns:xlink="http://www.w3.org/1999/xlink">
  <defs>
    <linearGradient id="blue-v" x1="0" y1="0" x2="0" y2="1">
      <stop offset="0" stop-color="var(--blue-light)"/>
      <stop offset="1" stop-color="var(--blue-dark)"/>
    </linearGradient>
    <linearGradient id="blue-h" x1="0" y1="0" x2="1" y2="0">
      <stop offset="0" stop-color="var(--blue-dark)"/>
      <stop offset="1" stop-color="var(--blue-light)"/>
    </linearGradient>
    <linearGradient id="orange-v" x1="0" y1="0" x2="0" y2="1">
      <stop offset="0" stop-color="var(--orange-light)"/>
      <stop offset="1" stop-color="var(--orange-dark)"/>
    </linearGradient>
    <linearGradient id="portrait-tone" x1="0" y1="0" x2="1" y2="1">
      <stop offset="0" stop-color="#e9d3bd"/>
      <stop offset="0.55" stop-color="#b07a52"/>
      <stop offset="1" stop-color="#3a2e2a"/>
    </linearGradient>
    <pattern id="grid-cell" width="12" height="12" patternUnits="userSpaceOnUse">
      <path d="M12 0H0V12" fill="none" stroke="var(--grid)" stroke-width="0.6"/>
    </pattern>
    <path id="plus-mark" d="M-5 -16H5V-5H16V5H5V16H-5V5H-16V-5H-5Z" fill="url(#orange-v)"/>

    <g id="model-chart">
      <!-- WHO box -->
      <rect x="78" y="393" width="110" height="100" rx="6" fill="#fff" stroke="url(#blue-v)" stroke-width="3"/>
      <text class="box-copy" x="86" y="417">▸ Drivers</text>
      <text class="box-copy" x="86" y="435">▸ Objectives</text>
      <text class="box-copy" x="86" y="453">▸ Benefits</text>
      <!-- WHAT box -->
      <rect x="200" y="365" width="113" height="128" rx="6" fill="#fff" stroke="url(#blue-v)" stroke-width="3"/>
      <rect x="200" y="365" width="113" height="30" rx="5" fill="url(#blue-v)"/>
      <text class="head-label" x="257" y="388">WHAT</text>
      <text class="box-copy" x="206" y="417">▸ Process</text>
      <text class="box-copy" x="206" y="435">▸ Organization</text>
      <text class="box-copy" x="206" y="453">▸ Capability</text>
      <!-- HOW box -->
      <rect x="326" y="393" width="110" height="100" rx="6" fill="#fff" stroke="url(#blue-v)" stroke-width="3"/>
      <text class="box-copy" x="331" y="417">▸ Enabling</text>
      <text class="box-copy" x="345" y="432">Project</text>
      <text class="box-copy" x="331" y="453">▸ Technology</text>
      <!-- tabs -->
      <rect x="92" y="463" width="83" height="32" rx="5" fill="url(#orange-v)"/>
      <text class="tab-label" x="133" y="486">WHO</text>
      <rect x="215" y="463" width="85" height="32" rx="5" fill="url(#orange-v)"/>
      <text class="tab-label" x="257" y="486">WHERE</text>
      <rect x="338" y="463" width="84" height="32" rx="5" fill="url(#orange-v)"/>
      <text class="tab-label" x="380" y="486">HOW</text>
      <!-- connectors -->
      <path d="M313 375H380V388" fill="none" stroke="var(--blue-light)" stroke-width="4"/>
      <path d="M373 387H387L380 396Z" fill="var(--blue-light)"/>
      <path d="M148 507V520H242V507" fill="none" stroke="var(--blue-dark)" stroke-width="4"/>
      <path d="M141 508H155L148 499Z M235 508H249L242 499Z" fill="var(--blue-dark)"/>
      <path d="M129 505H137V540H145L133 557L121 540H129Z" fill="url(#blue-v)"/>
      <path d="M253 505H261V540H269L257 557L245 540H253Z" fill="url(#blue-v)"/>
      <path d="M376 505H384V540H392L380 557L368 540H376Z" fill="url(#blue-v)"/>
      <!-- bars -->
      <rect x="53" y="563" width="410" height="33" rx="5" fill="url(#blue-v)"/>
      <text class="bar-label" x="258" y="587">WHO</text>
      <rect x="480" y="563" width="202" height="33" rx="5" fill="url(#blue-v)"/>
      <text class="bar-label" x="581" y="587">WHEN</text>
      <!-- timeline grid -->
      <rect x="485" y="390" width="182" height="130" fill="url(#grid-cell)"/>
      <rect x="508" y="410" width="106" height="13" rx="3" fill="url(#orange-v)"/>
      <rect x="538" y="447" width="87" height="13" rx="3" fill="url(#orange-v)"/>
      <rect x="490" y="483" width="50" height="14" rx="3" fill="url(#orange-v)"/>
      <rect x="570" y="483" width="80" height="14" rx="3" fill="url(#orange-v)"/>
      <path d="M487 530H668" stroke="var(--blue-light)" stroke-width="3"/>
      <path d="M666 525L677 530L666 535Z" fill="var(--blue-light)"/>
    </g>
  </defs>

  <!-- Section: model chart with presenter -->
  <g class="section model-with-presenter">
    <use href="#model-chart" transform="translate(12 -226.6) scale(0.744)"/>
    <rect x="505" y="55" width="185" height="213" fill="url(#portrait-tone)" role="img" aria-label="Illustration of a businesswoman drawing the model chart with a marker"/>
    <text class="caption" x="51" y="258">Model Chart + Female Illustration</text>
    <line class="rule" x1="33" y1="268.5" x2="702" y2="268.5"/>
  </g>

  <!-- Section: model chart -->
  <g class="section model-chart">
    <use href="#model-chart"/>
    <text class="caption" x="51" y="622">Model Chart</text>
    <line class="rule" x1="33" y1="638.5" x2="702" y2="638.5"/>
  </g>

  <!-- Section: presenter -->
  <g class="section presenter">
    <rect x="110" y="690" width="515" height="302" fill="url(#portrait-tone)" role="img" aria-label="Illustration of a businesswoman in a dark blazer holding a marker"/>
    <text class="caption" x="51" y="984">Female Illustration</text>
    <line class="rule" x1="33" y1="992.5" x2="702" y2="992.5"/>
  </g>

  <!-- Tagline option 1 -->
  <g class="section tagline-large">
    <text class="caption" x="51" y="1067">Tagline Illustration Option 1</text>
    <rect x="113" y="1088" width="509" height="62" rx="31" fill="url(#blue-v)"/>
    <g class="pill-copy" font-size="26">
      <text x="124" y="1129" font-size="32">(</text>
      <text x="145" y="1128">People</text>
      <text x="287" y="1128">Process</text>
      <text x="445" y="1128">Technology</text>
      <text x="596" y="1129" font-size="32">)</text>
    </g>
    <use href="#plus-mark" transform="translate(260 1119)"/>
    <use href="#plus-mark" transform="translate(417 1119)"/>
    <use href="#plus-mark" transform="translate(141 1189) rotate(45) scale(1.5)"/>
    <rect x="180" y="1160" width="152" height="60" rx="28" fill="url(#blue-v)"/>
    <text class="pill-copy center" x="256" y="1200" font-size="27">Planning</text>
    <rect x="345" y="1171" width="53" height="13" rx="2" fill="url(#orange-v)"/>
    <rect x="345" y="1194" width="53" height="13" rx="2" fill="url(#orange-v)"/>
    <rect x="410" y="1160" width="212" height="60" rx="28" fill="url(#blue-v)"/>
    <text class="pill-copy center" x="516" y="1204" font-size="37" font-weight="400">SUCCESS</text>
  </g>

  <!-- Tagline option 2 -->
  <g class="section tagline-inline">
    <rect x="68" y="1315" width="297" height="37" rx="18" fill="url(#blue-v)"/>
    <g class="pill-copy" font-size="15">
      <text x="74" y="1340" font-size="19">(</text>
      <text x="86" y="1339">People</text>
      <text x="169" y="1339">Process</text>
      <text x="261" y="1339">Technology</text>
      <text x="350" y="1340" font-size="19">)</text>
    </g>
    <use href="#plus-mark" transform="translate(153 1333) scale(0.6)"/>
    <use href="#plus-mark" transform="translate(244 1333) scale(0.6)"/>
    <use href="#plus-mark" transform="translate(387 1333) rotate(45) scale(0.95)"/>
    <rect x="410" y="1315" width="88" height="37" rx="18" fill="url(#blue-v)"/>
    <text class="pill-copy center" x="454" y="1339" font-size="15">Planning</text>
    <rect x="506" y="1323" width="32" height="8" rx="1" fill="url(#orange-v)"/>
    <rect x="506" y="1337" width="32" height="8" rx="1" fill="url(#orange-v)"/>
    <rect x="545" y="1315" width="122" height="37" rx="18" fill="url(#blue-v)"/>
    <text class="pill-copy center" x="606" y="1342" font-size="23" font-weight="400">SUCCESS</text>
    <text class="caption" x="51" y="1379">Tagline Illustration Option 2</text>
  </g>

  <!-- Tagline option 3 -->
  <g class="section tagline-banner">
    <rect x="106" y="1446" width="524" height="164" rx="3" fill="url(#blue-v)"/>
    <g class="pill-copy" font-size="21">
      <text x="118" y="1486" font-size="26">(</text>
      <text x="134" y="1484">People</text>
      <text x="238" y="1484">Process</text>
      <text x="355" y="1484">Technology</text>
      <text x="478" y="1486" font-size="26">)</text>
      <text x="524" y="1484">Planning</text>
    </g>
    <use href="#plus-mark" transform="translate(222 1477) scale(0.55)"/>
    <use href="#plus-mark" transform="translate(338 1477) scale(0.55)"/>
    <use href="#plus-mark" transform="translate(509 1477) rotate(45) scale(0.55)"/>
    <rect x="128" y="1498" width="485" height="3" fill="#fff"/>
    <text class="pill-copy" x="118" y="1590" font-size="100" font-weight="700" textLength="500" lengthAdjust="spacingAndGlyphs">SUCCESS</text>
    <text class="caption" x="51" y="1637">Tagline Illustration Option 3</text>
    <line class="rule" x1="33" y1="1660.5" x2="702" y2="1660.5"/>
  </g>

  <!-- Circular option 1 -->
  <g class="section methodology-band">
    <text class="caption" x="51" y="1687">Circular Illustration Option 1</text>
    <rect x="92" y="1705" width="553" height="193" rx="96" fill="url(#blue-h)"/>
    <path d="M265 1705H405L445 1742L405 1780H265L302 1742Z" fill="#1583cf"/>
    <path d="M410 1705H550L590 1742L550 1780H410L448 1742Z" fill="#1f98de"/>
    <path d="M372 1825H560V1898H372L332 1862Z" fill="#1173bf"/>
    <text class="pill-copy center" x="199" y="1751" font-size="21">Assessment</text>
    <text class="pill-copy center" x="357" y="1751" font-size="21">Design</text>
    <text class="pill-copy center" x="504" y="1751" font-size="21">Envision</text>
    <rect x="165" y="1780" width="405" height="45" rx="22" fill="#fff"/>
    <text class="methodology-label" x="368" y="1813">OUR METHODOLOGY</text>
    <text class="pill-copy center" x="243" y="1868" font-size="21">Implement</text>
    <text class="pill-copy center" x="483" y="1868" font-size="21">Implement</text>
  </g>

  <!-- Circular option 2 -->
  <g class="section methodology-cycle">
    <text class="caption" x="51" y="1977">Circular Illustration Option 2</text>
    <path d="M373.2,2010.1 A150,150 0 0 1 505.0,2099.0 L474.7,2129.4 L433.8,2130.7 A72,72 0 0 0 370.5,2088.0 L387.3,2050.7 Z" fill="url(#blue-v)"/>
    <path d="M512.2,2118.7 A150,150 0 0 1 468.4,2271.5 L430.1,2252.0 L416.2,2213.5 A72,72 0 0 0 437.2,2140.2 L477.9,2144.5 Z" fill="url(#blue-h)"/>
    <path d="M451.9,2284.4 A150,150 0 0 1 293,2289.9 L299.7,2247.5 L332,2222.4 A72,72 0 0 0 408.3,2219.7 L416.7,2259.8 Z" fill="url(#blue-v)"/>
    <path d="M275.6,2278.2 A150,150 0 0 1 221.3,2128.8 L263.7,2122.0 L297.6,2145.0 A72,72 0 0 0 323.7,2216.7 L288.2,2237.1 Z" fill="url(#blue-h)"/>
    <path d="M227.0,2108.7 A150,150 0 0 1 352.3,2010.8 L371.9,2049.1 L360.5,2088.4 A72,72 0 0 0 300.3,2135.4 L270.0,2107.9 Z" fill="url(#blue-v)"/>
    <circle cx="368" cy="2160" r="68" fill="url(#orange-v)"/>
    <text class="pill-copy center" x="368" y="2150" font-size="23">OUR</text>
    <text class="pill-copy center" x="368" y="2170" font-size="14">METHODOLOGY</text>
    <path id="cycle-track" d="M200,2160 A168,168 0 1 1 536,2160 A168,168 0 1 1 200,2160" fill="none"/>
    <text class="cycle-label" text-anchor="middle"><textPath href="#cycle-track" startOffset="132">Assessment</textPath></text>
    <text class="cycle-label" text-anchor="middle"><textPath href="#cycle-track" startOffset="337">Envision</textPath></text>
    <text class="cycle-label" text-anchor="middle"><textPath href="#cycle-track" startOffset="560">Design</textPath></text>
    <text class="cycle-label" text-anchor="middle"><textPath href="#cycle-track" startOffset="765">Evaluate</textPath></text>
    <text class="cycle-label" text-anchor="middle"><textPath href="#cycle-track" startOffset="967">Implement</textPath></text>
  </g>
</svg>
</body>
</html>
```